Branding label contest for 2 great products

I require labels for our health food treat dry packs and coffee business. The packaging at this stage consists of the follow... plastic food pouches for dry ingredients and takeaway coffee cups. The coffee cup artwork/design will be for standard small, medium and large paper takeaway coffee cups and the food pouch size 190mmW x 260mmL. the pouch design will need to be customisable to allow use across a range of products. for reference please visit www.torvimelu.com.au and instagram @torvimelu for products. I have attached our logo and business card files for your perusal.

Target Market(s)

Healthy conscious, vegan, paleo, gluten free, all round fitness fanatics and yogis

Industry/Entity Type

Business

Requirements
Must have
• Earthy tones, our logo. Rustic earthy feel. trendy artwork.
Should not have
• Bright colours

```html
<!DOCTYPE html>
<html lang="en">
<head>
<meta charset="utf-8">
<title>Torvimelu Goji Berries Pouch Label</title>
<link href="https://fonts.googleapis.com/css2?family=Bebas+Neue&family=Amatic+SC:wght@700&family=Zilla+Slab:wght@500&display=swap" rel="stylesheet">
<style>
  :root {
    --canvas: #ffffff;
    --pouch-clear: #eeeeef;
    --pouch-clear-edge: #dcdcde;
    --berry-light: #c25a48;
    --berry-mid: #a8412f;
    --berry-dark: #7f2a20;
    --kraft: #c59c66;
    --kraft-shade: #b98e58;
    --ink: #6a3e31;
    --badge: #ffffff;
  }
  * { margin: 0; padding: 0; box-sizing: border-box; }
  html, body { width: 1200px; height: 1200px; overflow: hidden; background: var(--canvas); }
  .canvas { position: relative; width: 1200px; height: 1200px; }

  .pouch { position: absolute; left: 258px; top: 84px; width: 684px; height: 1100px; }
  .pouch-window {
    position: absolute; inset: 0 0 auto 0; height: 210px;
    background: linear-gradient(180deg, var(--pouch-clear) 0%, #f7f7f8 60%, var(--pouch-clear) 100%);
    border: 1px solid var(--pouch-clear-edge); border-bottom: none;
  }
  .zip-seal { position: absolute; left: 0; right: 0; top: 160px; height: 3px; background: var(--pouch-clear-edge); }
  .pouch-contents {
    position: absolute; left: 0; right: 0; top: 204px; bottom: 0;
    background:
      radial-gradient(circle at 20% 30%, var(--berry-light) 0, transparent 40%),
      radial-gradient(circle at 80% 70%, var(--berry-light) 0, transparent 45%),
      linear-gradient(160deg, var(--berry-mid), var(--berry-dark));
  }

  .label {
    position: absolute; left: 432px; top: 352px; width: 338px; height: 762px;
    background: linear-gradient(170deg, var(--kraft), var(--kraft-shade));
    color: var(--ink); text-align: center;
  }
  .brand-badge {
    position: absolute; left: 508px; top: 262px; width: 164px; height: 164px;
    border-radius: 50%; background: var(--badge);
    display: flex; align-items: center; justify-content: center;
  }
  .brand-name { font-family: "Zilla Slab", serif; font-weight: 500; font-size: 24px; letter-spacing: 2px; color: var(--ink); }

  .product-name { font-family: "Bebas Neue", sans-serif; font-weight: 400; line-height: 1; }
  .product-name span { position: absolute; left: 0; right: 0; white-space: nowrap; }
  .product-name .line-1 { top: 132px; font-size: 152px; letter-spacing: 4px; }
  .product-name .line-2 { top: 268px; font-size: 112px; letter-spacing: 1px; }
  .tagline {
    position: absolute; left: 0; right: 0; top: 392px;
    font-family: "Amatic SC", sans-serif; font-weight: 700; font-size: 56px; line-height: 1; letter-spacing: 2px;
    white-space: nowrap;
  }
  .flower-mark { position: absolute; left: 112px; top: 482px; width: 120px; height: 106px; border-radius: 50%; background: var(--kraft-shade); opacity: .9; }
  .divider { position: absolute; left: 26px; width: 286px; height: 2px; }
  .divider.top { top: 613px; }
  .divider.bottom { top: 729px; }
  .diet-list {
    position: absolute; left: 0; right: 0; top: 632px;
    font-family: "Zilla Slab", serif; font-weight: 500; font-size: 24px; line-height: 29px;
  }
</style>
</head>
<body>
<main class="canvas">
  <div class="pouch">
    <div class="pouch-window"><div class="zip-seal"></div></div>
    <div class="pouch-contents" role="img" aria-label="Dried goji berries filling the pouch"></div>
  </div>

  <section class="label">
    <h1 class="product-name"><span class="line-1">GOJI</span><span class="line-2">BERRIES</span></h1>
    <p class="tagline">BETTER FOR YOU</p>
    <div class="flower-mark" role="img" aria-label="Hand-drawn flower illustration"></div>
    <svg class="divider top" viewBox="0 0 286 2"><line x1="0" y1="1" x2="286" y2="1" stroke="#6a3e31" stroke-width="2" stroke-dasharray="10 7"/></svg>
    <p class="diet-list">vegan, gluten-free,<br>paleo, dairy-free,<br>grain-free</p>
    <svg class="divider bottom" viewBox="0 0 286 2"><line x1="0" y1="1" x2="286" y2="1" stroke="#6a3e31" stroke-width="2" stroke-dasharray="10 7"/></svg>
  </section>

  <div class="brand-badge"><span class="brand-name">TORVIMELU</span></div>
</main>
</body>
</html>
```